Business cards for a high-end menswear store

I would like to come up with a design for our business cards.
Two different ones: one for general sales and one for the owner. It is a high-end menswear store.

Our address is: 4817 Morneau Boulevard, Montreal, QC, K7P4M2
phone number: 514-286-5937
insta: MAISONVERLAINE
Website: www.maisonverlaine.example
email (general card): info@maisonverlaine.example
email (owner): bastien@maisonverlaine.example

I have attached our logo in an ai and eps file format. You can see our old cards as well. I am looking for a modern and clean look.

Target Market(s)

High-End Clothing Market

Industry/Entity Type

Retail, Clothing, Luxury Clothing

Contact Information for Business Card

Address, Name, Email, Website, Social Info,

Font styles to use
Serif

Colors

Designer to choose colors to be used in the design.

Requirements
Must have
• Address, Name, Email, Website, Social Info,
Nice to have
• QR Code that brings you to the website

```html
<!DOCTYPE html>
<html lang="en">
<head>
<meta charset="utf-8">
<title>Maison Verlaine — Business Cards</title>
<link href="https://fonts.googleapis.com/css2?family=Playfair+Display:wght@600;700&family=Raleway:wght@300;400;600&display=swap" rel="stylesheet">
<style>
  :root {
    --ink: #1f1d1e;
    --stage: #2a2a2c;
    --paper: #ffffff;
    --gold: #d9ad35;
    --gold-light: #f0cf5e;
    --gold-deep: #b8891f;
    --silver: #d8d8d8;
  }
  * { box-sizing: border-box; margin: 0; padding: 0; }
  html, body { width: 1200px; height: 800px; overflow: hidden; }
  body {
    background: var(--stage);
    font-family: "Raleway", sans-serif;
    position: relative;
  }

  /* ---------- Owner card (vertical, contact side) ---------- */
  .card-owner {
    position: absolute;
    left: 130px; top: 102px;
    width: 340px; height: 596px;
    background: var(--ink);
    overflow: hidden;
    box-shadow: 0 18px 40px rgba(0,0,0,.45);
  }
  .card-owner__top {
    position: absolute; left: 0; right: 0; top: 0;
    height: 262px;
    background: var(--paper);
  }
  .card-owner__frame {
    position: absolute;
    inset: 20px;
    border: 5px solid var(--gold);
  }
  .brand {
    position: absolute;
    display: flex; align-items: center; gap: 12px;
    font-family: "Playfair Display", serif;
    font-weight: 600;
    letter-spacing: .08em;
    white-space: nowrap;
  }
  .brand__square { display: block; flex: none; }
  .card-owner .brand {
    left: 50%; top: 131px;
    transform: translate(-50%, -50%);
    font-size: 20px;
    color: var(--ink);
  }
  .card-owner .brand__square { width: 26px; height: 26px; background: var(--ink); }

  .contact {
    position: absolute;
    left: 0; right: 0; top: 290px;
    text-align: center;
    color: var(--silver);
  }
  .contact__name {
    font-family: "Playfair Display", serif;
    font-weight: 700;
    font-size: 23px;
    letter-spacing: .02em;
    color: var(--paper);
    text-transform: uppercase;
  }
  .contact__role {
    font-weight: 300;
    font-size: 13px;
    letter-spacing: .06em;
    margin-top: 2px;
    color: var(--paper);
  }
  .contact__rule {
    width: 22px; height: 3px;
    background: var(--gold);
    margin: 12px auto 10px;
  }
  .contact__address {
    font-weight: 300;
    font-size: 12.5px;
    line-height: 1.45;
  }
  .contact__icons {
    display: flex; justify-content: center; gap: 12px;
    margin: 14px 0 10px;
  }
  .contact__icons svg { width: 15px; height: 15px; }
  .contact__phone {
    font-weight: 600;
    font-size: 15px;
    color: var(--paper);
    letter-spacing: .03em;
  }
  .contact__line {
    font-weight: 300;
    font-size: 12.5px;
    line-height: 1.55;
  }

  /* ---------- General card (horizontal, brand side) ---------- */
  .card-brand {
    position: absolute;
    left: 530px; top: 230px;
    width: 580px; height: 332px;
    background: var(--ink);
    box-shadow: 0 18px 40px rgba(0,0,0,.45);
  }
  .card-brand .brand {
    left: 50%; top: 50%;
    transform: translate(-50%, -50%);
    font-size: 30px;
    gap: 20px;
    color: var(--gold);
  }
  .card-brand .brand__square {
    width: 120px; height: 120px;
    background: linear-gradient(135deg, var(--gold-light), var(--gold) 45%, var(--gold-deep));
  }
</style>
</head>
<body>

  <section class="card-owner" aria-label="Owner business card">
    <div class="card-owner__top"></div>
    <div class="card-owner__frame"></div>

    <div class="brand">
      <span class="brand__square"></span>
      <span class="brand__name">MAISON VERLAINE</span>
    </div>

    <div class="contact">
      <p class="contact__name">Bastien Lacroix</p>
      <p class="contact__role">Co-President</p>
      <div class="contact__rule"></div>
      <p class="contact__address">4817 Morneau Boulevard,<br>Montreal, QC, K7P4M2</p>

      <div class="contact__icons">
        <svg viewBox="0 0 16 16" aria-label="Phone"><path fill="var(--gold)" d="M4 1.5l2.2 3-1.3 1.4c.8 1.9 2.3 3.4 4.2 4.2l1.4-1.3 3 2.2-1.2 2.6C7 13.4 2.6 9 2.2 2.7z"/></svg>
        <svg viewBox="0 0 16 16" aria-label="Social"><circle cx="8" cy="8" r="6.5" fill="var(--gold)"/></svg>
        <svg viewBox="0 0 16 16" aria-label="Email"><rect x="1.5" y="3.5" width="13" height="9" fill="var(--gold)"/><path d="M1.5 3.5l6.5 5 6.5-5" fill="none" stroke="var(--ink)" stroke-width="1.2"/></svg>
        <svg viewBox="0 0 16 16" aria-label="Website"><circle cx="8" cy="8" r="6.5" fill="var(--gold)"/><path d="M1.5 8h13M8 1.5c2.5 2.5 2.5 10.5 0 13M8 1.5c-2.5 2.5-2.5 10.5 0 13" fill="none" stroke="var(--ink)" stroke-width="1"/></svg>
      </div>

      <p class="contact__phone">514-286-5937</p>
      <p class="contact__line">MAISONVERLAINE</p>
      <p class="contact__line">bastien@maisonverlaine.example</p>
      <p class="contact__line">www.maisonverlaine.example</p>
    </div>
  </section>

  <section class="card-brand" aria-label="General business card">
    <div class="brand">
      <span class="brand__square"></span>
      <span class="brand__name">MAISON VERLAINE</span>
    </div>
  </section>

</body>
</html>
```